KAY VELORE

We need a letterhead design for an Image & Etiquette Consultancy company based in Singapore.

The services we provide are Personal Image Consultation, Image & Etiquette Workshop for schools and corporate.

The design should have our corporate colour as seen in the logo files I have uploaded.

Since our company helps clients with their image, the design should be aesthetically very appealing. It should reflect a very classy & elegant feel.

I will print the letterhead using my printer but most of the time will use it to write letters to my clients therefore the format should include MS Word.

```html
<!DOCTYPE html>
<html lang="en">
<head>
<meta charset="utf-8">
<title>Kay Velore Letterhead</title>
<link href="https://fonts.googleapis.com/css2?family=Jura:wght@500&family=Open+Sans:wght@600&display=swap" rel="stylesheet">
<style>
  :root {
    --brand-purple: #341450;
    --brand-gold: #c9a13b;
    --paper: #ffffff;
    --muted-grey: #dedbce;
    --contact-white: #ffffff;
  }
  * { margin: 0; padding: 0; box-sizing: border-box; }
  html, body { width: 971px; height: 1200px; overflow: hidden; background: var(--paper); }
  .letterhead { position: relative; width: 971px; height: 1200px; background: var(--paper); }

  .header-band {
    position: absolute; left: 0; top: 0; width: 971px; height: 134px;
    background: var(--brand-purple);
  }
  .brand-name {
    position: absolute; left: 62px; top: 0; height: 134px;
    display: flex; align-items: center;
    font-family: "Jura", sans-serif; font-weight: 500;
    font-size: 72px; line-height: 1; letter-spacing: 1px;
    color: var(--brand-gold); white-space: nowrap;
  }

  .contact-list {
    position: absolute; right: 46px; top: 44px;
    list-style: none; text-align: right;
    font-family: "Open Sans", sans-serif; font-weight: 600;
    color: var(--contact-white);
  }
  .contact-item {
    display: flex; justify-content: flex-end; align-items: center;
    gap: 8px; height: 23px; font-size: 15px; letter-spacing: 0.6px;
  }
  .contact-item.phone { font-size: 17px; letter-spacing: 1px; }
  .contact-icon { width: 15px; height: 15px; flex: none; }

  .footer-band {
    position: absolute; left: 0; top: 1143px; width: 659px; height: 18px;
    background: var(--brand-purple);
  }
  .footer-mark {
    position: absolute; left: 690px; top: 1132px;
    font-family: "Jura", sans-serif; font-weight: 500;
    font-size: 42px; line-height: 1; letter-spacing: 1px;
    color: var(--muted-grey); white-space: nowrap;
  }
</style>
</head>
<body>
<main class="letterhead">
  <header class="header-band">
    <div class="brand-name">KAY VELORE</div>
    <ul class="contact-list">
      <li class="contact-item phone">0198765432
        <svg class="contact-icon" viewBox="0 0 16 16" aria-hidden="true"><rect x="4.5" y="1" width="7" height="14" rx="1.5" fill="none" stroke="#fff" stroke-width="1.6"/><line x1="7" y1="12.5" x2="9" y2="12.5" stroke="#fff" stroke-width="1.6"/></svg>
      </li>
      <li class="contact-item">studio@velorepoise.com
        <svg class="contact-icon" viewBox="0 0 16 16" aria-hidden="true"><rect x="1.5" y="3.5" width="13" height="9" rx="1" fill="none" stroke="#fff" stroke-width="1.6"/><polyline points="1.5,4 8,9 14.5,4" fill="none" stroke="#fff" stroke-width="1.6"/></svg>
      </li>
      <li class="contact-item">velorepoise.com
        <svg class="contact-icon" viewBox="0 0 16 16" aria-hidden="true"><g fill="none" stroke="#fff" stroke-width="1.3"><circle cx="8" cy="8" r="6.5"/><ellipse cx="8" cy="8" rx="3" ry="6.5"/><line x1="1.5" y1="8" x2="14.5" y2="8"/></g></svg>
      </li>
    </ul>
  </header>

  <footer>
    <div class="footer-band"></div>
    <div class="footer-mark">KAY VELORE</div>
  </footer>
</main>
</body>
</html>
```